Tree Service Billboard 20x8 ft

We need a billboard design for a tree service company.
The billboard is 20ft x 8 ft so we need a design that is capable to stretching to those dimensions without loosing quality.
I have attached a series of images.
Image 1- Simply a billboard that I think looks good that I would like you to use for inspiration. I am aiming for the same format only no color in the wording, just black white, or gray. I like the the trees in the background, the logo placed to the left, and wording on the right.
Image 2- Current Logo I would like to the left of the billboard
Image 3- Another format of current logo if needed.
Image 4- A drawn out design template
Image 5- Another drawn out design template

Specific things I am looking for
-The contact number to be the largest thing on the design
-The logo on the design
-Key points to the design to say:
Tree Removal
Tree Trimming
Land Development
Stump Grinding
Storm Response
Insured
Free Bids
-The facebook logo
-The Google Logo

```html
<!DOCTYPE html>
<html lang="en">
<head>
<meta charset="utf-8">
<title>Ash's Tree Service — Billboard</title>
<link rel="stylesheet" href="https://fonts.googleapis.com/css2?family=Bebas+Neue&family=Orbitron:wght@700;900&display=swap">
<style>
  :root {
    --page: #ffffff;
    --ink: #000000;
    --paper: #ffffff;
    --steel: #808080;
    --icon-grey: #7a7a7a;
    --forest-light: #8fb59a;
    --forest-mid: #3f7a45;
    --forest-deep: #1f4a22;
  }
  * { margin: 0; padding: 0; box-sizing: border-box; }
  html, body {
    width: 1200px; height: 655px; overflow: hidden;
    background: var(--page);
  }
  .billboard {
    position: absolute; left: 54px; top: 109px;
    width: 1091px; height: 436px;
    overflow: hidden;
  }
  .forest-backdrop {
    position: absolute; left: 0; top: 0; width: 100%; height: 364px;
    background:
      linear-gradient(180deg, var(--forest-light) 0%, #6e9f78 28%, var(--forest-mid) 55%, var(--forest-deep) 100%);
  }
  .brand-seal {
    position: absolute; left: 150px; top: 14px;
    width: 268px; height: 268px; border-radius: 50%;
    background: var(--paper);
  }
  .brand-name {
    position: absolute; left: 46px; top: 290px; width: 474px;
    font-family: "Bebas Neue", sans-serif;
    font-size: 66px; line-height: 1;
    color: var(--paper); text-align: center;
    letter-spacing: 0.02em; white-space: nowrap;
  }
  .service-list {
    position: absolute; left: 599px; top: 25px; width: 492px;
    list-style: none;
  }
  .service-list li {
    height: 41px; margin-bottom: 6.5px;
    padding-right: 47px;
    display: flex; align-items: center; justify-content: flex-end;
    font-family: "Orbitron", sans-serif; font-weight: 900;
    font-size: 27px; letter-spacing: 0.06em;
    white-space: nowrap;
  }
  .service-list li:nth-child(odd) { background: var(--ink); color: var(--paper); }
  .service-list li:nth-child(even) { background: var(--steel); color: var(--ink); }
  .contact-bar {
    position: absolute; left: 0; top: 364px; width: 100%; height: 72px;
    background: var(--ink);
    border-top: 4px solid var(--steel);
  }
  .phone-number {
    position: absolute; left: 29px; top: 9px;
    font-family: "Orbitron", sans-serif; font-weight: 700;
    font-size: 46px; letter-spacing: 0.14em; line-height: 1.1;
    color: var(--paper); white-space: nowrap;
  }
  .social-marks {
    position: absolute; left: 892px; top: 9px;
    width: 140px; height: 52px;
  }
</style>
</head>
<body>
  <main class="billboard">
    <div class="forest-backdrop" role="img" aria-label="Photo of misty forested green mountains"></div>

    <div class="brand-seal" aria-hidden="true"></div>
    <h1 class="brand-name">Ash's Tree Service</h1>

    <ul class="service-list">
      <li>TREE REMOVAL</li>
      <li>TREE TRIMMING</li>
      <li>LAND DEVELOPMENT</li>
      <li>STUMP GRINDING</li>
      <li>STORM RESPONSE</li>
      <li>INSURED</li>
      <li>FREE BIDS</li>
    </ul>

    <footer class="contact-bar">
      <p class="phone-number">555-014-2876</p>
      <svg class="social-marks" viewBox="0 0 140 52" aria-hidden="true">
        <circle cx="26" cy="26" r="23" fill="none" stroke="var(--icon-grey)" stroke-width="3"/>
        <circle cx="100" cy="26" r="23" fill="none" stroke="var(--icon-grey)" stroke-width="3"/>
      </svg>
    </footer>
  </main>
</body>
</html>
```